Re-design of professional audio retail website brevlando.co.nz

Our current website brevlando.co.nz is now 20 years old and needs a refresh. All our customers love the easy navigation style so we would like to keep a similar style of top navigation bar and the drop down Products, Categories, sub categories etc, menu on the left that stays there on all pages except the front page. For each category page the right hand pane is to have icons for the sub categories like our current site
So in essence all the same functionality and similar layout of the old website but just smartened up to make it look more modern.
We like the the darker blue background colours in the old website and would like it to have some kind of subtle audio/sound theme to it like the waveforms used in the old one.
We would like the main front landing page designed, plus the sub categories icons page including the style of left side category/sub category navigation. Plus some ideas for a product page.
Main front page to have similar components to current website. ie Content carousel, browse categories, brands, some specials/new products
If you've submitted a logo to our other design request then feel free to use that on this design as we’ve not chosen the winner from that yet. If you’ve not designed a logo then use our existing one

Target Market(s)

Musicians, schools, churches, theatres, DJ's

Industry/Entity Type

Professional audio, sound systems, DJ gear.

Font styles to use
Sans Serif

Colors

Designer to choose colors to be used in the design.

Requirements
Must have
• Product images on white background. Search engine field at top right always visible. Drop down left side navigation/filtering bar that is there all the time once off the main index page. Darker blue background. Top menu bar with tabs for Products (that drops down to categories), Special Offers, Brands, Discounts, About Us, Contact Us.
Nice to have
• A tech or audio feel to it, some subtle reference to audio waveforms in the backgroundmaybe

```html
<!DOCTYPE html>
<html lang="en">
<head>
<meta charset="utf-8">
<title>brevlando — Customer Sign In</title>
<link rel="stylesheet" href="https://fonts.googleapis.com/css2?family=Inter:wght@400;500;600&family=Outfit:wght@600;700;800&display=swap">
<style>
  :root{
    --bg:#040716;
    --bg-panel:#0a1128;
    --hero-a:#120f24;
    --hero-b:#3a2a35;
    --modal:#111831;
    --modal-edge:#2d77b3;
    --field:#0b1022;
    --field-edge:#2a3250;
    --text:#ffffff;
    --label:#d7dcea;
    --muted:#8a93ad;
    --link:#39aef2;
    --btn-a:#42b3f6;
    --btn-b:#3f68ff;
    --btn-text:#0b1430;
    --accent:#2f7ff0;
    --badge:#6b2fc9;
    --card:#2b2f3d;
  }
  *{box-sizing:border-box;margin:0;padding:0}
  html,body{width:1200px;height:936px;overflow:hidden;background:var(--bg);font-family:"Inter",sans-serif}
  .stage{position:relative;width:1200px;height:936px;overflow:hidden}

  /* blurred storefront behind the dialog */
  .page{position:absolute;left:0;top:0;width:1200px;height:936px;overflow:hidden;filter:blur(7px);opacity:.55;color:#c9d2ea}
  .brand{position:absolute;left:138px;top:10px;font:700 22px "Outfit",sans-serif;color:#b9c3dc}
  .tagline{position:absolute;left:440px;top:20px;font-size:12px;color:#6c7896}
  .search{position:absolute;left:782px;top:16px;width:56px;height:18px;border-radius:9px;background:var(--accent)}
  .util{position:absolute;top:18px;font-size:12px;color:#7a86a6}
  .main-nav{position:absolute;left:76px;top:74px;display:flex;gap:34px;font-size:12px;color:#7f8aa8}
  .hero{position:absolute;left:110px;top:128px;width:969px;height:307px;border-radius:8px;
        background:linear-gradient(90deg,var(--hero-a) 35%,var(--hero-b) 100%)}
  .eyebrow{position:absolute;left:44px;top:60px;font-size:11px;color:var(--accent)}
  .hero h1{position:absolute;left:44px;top:88px;font:700 31px "Outfit",sans-serif;color:#dfe4f2}
  .hero p{position:absolute;left:44px;top:134px;width:430px;font-size:12px;line-height:20px;color:#8390ad}
  .hero .cta{position:absolute;left:44px;top:220px;width:139px;height:25px;border-radius:13px;background:var(--accent);
             font-size:11px;color:#fff;padding:6px 18px}
  .tabs{position:absolute;left:140px;top:494px;width:910px;display:flex;justify-content:space-between;font-size:11px;color:#5e6a88}
  .section-title{position:absolute;left:110px;font:700 22px "Outfit",sans-serif;color:#c7cfe3}
  .section-title::before{content:"";display:inline-block;width:10px;height:10px;border-radius:50%;background:var(--accent);margin-right:10px}
  .cats{position:absolute;left:102px;top:637px;width:981px;height:157px;display:flex;gap:8px}
  .cat{flex:1;background:var(--bg-panel);border-radius:8px;text-align:center;padding-top:28px}
  .cat i{display:block;width:20px;height:20px;margin:0 auto 30px;border-radius:50%;background:#1c3a7a}
  .cat b{display:block;font-size:12px;color:#8f9ab5}
  .cat span{display:block;font-size:10px;color:#55607c;margin-top:10px}
  .product{position:absolute;top:900px;width:223px;height:36px;border-radius:8px 8px 0 0;background:var(--card)}
  .product em{position:absolute;left:12px;top:12px;width:84px;height:16px;border-radius:8px;background:var(--badge);
              font-style:normal;font-size:10px;color:#fff;padding:2px 10px}

  /* sign-in dialog */
  .dialog{position:absolute;left:410px;top:305px;width:364px;height:326px;border-radius:9px;background:var(--modal);
          border:1px solid var(--modal-edge);box-shadow:0 0 22px rgba(45,140,230,.35)}
  .close{position:absolute;right:16px;top:23px;width:9px;height:9px}
  .dialog h2{position:absolute;left:0;right:0;top:34px;text-align:center;font:800 22px "Outfit",sans-serif;color:var(--text);letter-spacing:-.4px}
  .field-label{position:absolute;left:29px;font-size:10.5px;font-weight:500;color:var(--label)}
  .field{position:absolute;left:29px;width:306px;height:31px;border-radius:5px;background:var(--field);border:1px solid var(--field-edge);
         font-size:10px;color:var(--muted);padding:8px 12px}
  .field.secret{letter-spacing:1.5px;font-size:11px;padding-top:7px;color:#c9cfe0}
  .login{position:absolute;left:29px;top:222px;width:306px;height:40px;border-radius:20px;
         background:linear-gradient(90deg,var(--btn-a),var(--btn-b));font:700 13px "Outfit",sans-serif;letter-spacing:.8px;color:var(--btn-text);
         display:flex;align-items:center;justify-content:center}
  .foot{position:absolute;left:29px;right:29px;top:280px;display:flex;justify-content:space-between;font-size:10.5px;color:var(--label)}
  .foot a{color:var(--link);font-weight:600;text-decoration:none}
</style>
</head>
<body>
<div class="stage">
  <div class="page" aria-hidden="true">
    <div class="brand">brevlando</div>
    <div class="tagline">Pro audio for stage and studio</div>
    <div class="search"></div>
    <div class="util" style="left:842px">Search</div>
    <div class="util" style="left:922px">Sign In · My Account</div>
    <div class="util" style="left:1056px">Cart</div>
    <nav class="main-nav"><span>Products</span><span>Special Offers</span><span>Brands</span><span>Discounts</span><span>About Us</span><span>Contact Us</span></nav>
    <section class="hero">
      <div class="eyebrow">New Arrivals</div>
      <h1>Precision Studio Monitoring</h1>
      <p>Reference monitors built for honest mixing, tight bass and clear detail at every level.</p>
      <div class="cta">Shop Monitors</div>
    </section>
    <div class="tabs"><span>Studio Monitors</span><span>PA Speakers</span><span>Mixers</span><span>Microphones</span><span>DJ Gear</span><span>Lighting</span></div>
    <h3 class="section-title" style="top:586px">Browse Categories</h3>
    <div class="cats">
      <div class="cat"><i></i><b>Speakers</b><span>24 products</span></div>
      <div class="cat"><i></i><b>Mixers</b><span>18 products</span></div>
      <div class="cat"><i></i><b>Microphones</b><span>31 products</span></div>
      <div class="cat"><i></i><b>Stands, Cables &amp; Cases</b><span>56 products</span></div>
    </div>
    <h3 class="section-title" style="top:849px">Featured Specials &amp; New Products</h3>
    <div class="product" style="left:106px"><em>New</em></div>
    <div class="product" style="left:355px"><em>Special</em></div>
  </div>

  <div class="dialog" role="dialog" aria-labelledby="signin-title">
    <svg class="close" viewBox="0 0 9 9" aria-label="Close"><path d="M1 1L8 8M8 1L1 8" stroke="#b8c0d4" stroke-width="1.2"/></svg>
    <h2 id="signin-title">CUSTOMER SIGN IN</h2>
    <div class="field-label" style="top:88px">Email Address</div>
    <div class="field" style="top:101px">name@email.com</div>
    <div class="field-label" style="top:153px">Password</div>
    <div class="field secret" style="top:166px">••••••••</div>
    <div class="login">LOG IN</div>
    <div class="foot"><span>Don't have an account? <a href="#">Create one</a></span><a href="#">Forgot Password?</a></div>
  </div>
</div>
</body>
</html>
```